Business Cards for Marco and Tobin

Design of business cards for two people with the recently created brand Valcor Mobile. Valcor Mobile wants to become a worldwide major player on the secondhand phone market. It gathers send hand phones from individuals, refurbish them and sell them throughout the world. It has a green impact (recycling) and we also contribute to social project in Africa (a percentage of our benefits are sent to build school, sport facilities, etc.

Target Market(s)

B2B - Marco and Tobin are in contact with distributors across Africa.

Industry/Entity Type

Wireless Communication

Contact Information for Business Card

Marco Feuillet
Head of Emerging Markets
Valcor Energy South Africa (Pty) Ltd
Kestrel Road 47
2031 Sandton - Johannesburg
South Africa
Tel: + 27 10 555 0148
Mobile : +27 82 55 104
Email : marco.feuillet@valcormobile.example
Skype: marco.feuillet
Web: www.valcormobile.example
 

Tobin Farrow
Head of Southern Africa
Kestrel Road 47
South Africa
Tel: + 27 10 555 0148
Mobile: +27 83 555 0276
Email: tobin.farrow@valcormobile.example
Skype: tobin.farrow
Web: www.valcormobile.example

Requirements
Must have
• The cards need to be "serious", trustable, with a worldwide presence.
Nice to have
• Some "green" / recycling touch would be nice but not necessary if in contradiction with the general design.

```html
<!DOCTYPE html>
<html lang="en">
<head>
<meta charset="utf-8">
<title>Valcor Mobile – Business Card</title>
<link rel="stylesheet" href="https://fonts.googleapis.com/css2?family=Source+Sans+3:wght@400;600;700&display=swap">
<style>
  :root {
    --page: #000000;
    --navy: #072c45;
    --sky: #2b94d2;
    --accent: #3399dd;
    --ink-dark: #0b3350;
    --white: #ffffff;
  }
  * { margin: 0; padding: 0; box-sizing: border-box; }
  html, body { width: 1200px; height: 900px; overflow: hidden; background: var(--page); }
  body { position: relative; font-family: "Source Sans 3", "Segoe UI", sans-serif; }

  .card { position: absolute; top: 275px; width: 477px; height: 293px; }
  .card-front { left: 116px; background: var(--navy); border-radius: 0 62px 0 62px; }
  .card-back { left: 622px; top: 276px; height: 292px; background: var(--sky); border-radius: 62px 0 62px 0; }

  .brand-mark { position: absolute; border-radius: 50%; }
  .card-front .brand-mark { left: 88px; top: 34px; width: 48px; height: 48px; background: var(--accent); }
  .card-front .brand-name {
    position: absolute; left: 32px; top: 128px;
    font-size: 27px; font-weight: 700; color: var(--white); letter-spacing: -0.3px; white-space: nowrap;
  }

  .holder { position: absolute; right: 19px; top: 34px; text-align: right; }
  .holder-name { font-size: 18px; font-weight: 600; color: var(--accent); line-height: 24px; }
  .holder-role { font-size: 13px; color: var(--white); line-height: 18px; }

  .contact-list { position: absolute; right: 19px; top: 122px; list-style: none; }
  .contact-list li {
    display: flex; justify-content: flex-end; align-items: center; gap: 7px;
    font-size: 13px; color: var(--white); line-height: 19.6px;
  }
  .contact-list svg { width: 11px; height: 11px; fill: var(--accent); flex: none; }

  .company { position: absolute; right: 20px; top: 238px; text-align: right; }
  .company-name { font-size: 13px; font-weight: 600; color: var(--accent); line-height: 19px; }
  .company-address { font-size: 13px; color: var(--white); line-height: 19px; white-space: nowrap; }

  .card-back .brand-mark { left: 208px; top: 66px; width: 62px; height: 62px; background: var(--white); }
  .card-back .brand-name {
    position: absolute; left: 0; right: 0; top: 194px; text-align: center;
    font-size: 36px; font-weight: 700; color: var(--ink-dark); letter-spacing: -0.4px;
  }
</style>
</head>
<body>
  <section class="card card-front">
    <span class="brand-mark"></span>
    <div class="brand-name">Valcor Mobile</div>

    <div class="holder">
      <div class="holder-name">Marco Feuillet</div>
      <div class="holder-role">Head of Emerging Markets</div>
    </div>

    <ul class="contact-list">
      <li>+ 27 10 555 0148
        <svg viewBox="0 0 12 12"><path d="M2.4 0.8l2 2.2-1 1.3c.8 1.6 2 2.8 3.6 3.6l1.3-1 2.2 2-1.2 1.9C5.5 11 1 6.5.5 2z"/></svg>
      </li>
      <li>+27 82 55 104
        <svg viewBox="0 0 12 12"><path d="M3 0h6a1 1 0 0 1 1 1v10a1 1 0 0 1-1 1H3a1 1 0 0 1-1-1V1a1 1 0 0 1 1-1zm.3 1.3v8.2h5.4V1.3z"/></svg>
      </li>
      <li>marco.feuillet@valcormobile.example
        <svg viewBox="0 0 12 12"><path d="M0 2h12v8H0zm1 1v.4l5 3.3 5-3.3V3z"/></svg>
      </li>
      <li>www.valcormobile.example
        <svg viewBox="0 0 12 12"><path d="M6 0a6 6 0 1 0 0 12A6 6 0 0 0 6 0zm-1 2.5l2 1-.5 2L8 7l-1 2.5-2-1.5V6.5L3 5.5z"/></svg>
      </li>
      <li>marco.feuillet
        <svg viewBox="0 0 12 12"><path d="M6 0a6 6 0 1 0 0 12A6 6 0 0 0 6 0zM3 3.5h6v4H5.5L3.8 9V7.5H3z"/></svg>
      </li>
    </ul>

    <div class="company">
      <div class="company-name">Valcor Energy South Africa (Pty) Ltd</div>
      <div class="company-address">Kestrel Road 47 2031 Sandton - Johannesburg South Africa</div>
    </div>
  </section>

  <section class="card card-back">
    <span class="brand-mark"></span>
    <div class="brand-name">Valcor Mobile</div>
  </section>
</body>
</html>
```